Painting Storms over Harbors Book Cover Design

Create a customized book cover for both digital and print versions of my new book. The book will be sold on Vellora, Pagemontix and also printed in soft cover. Need formatting to work for all formats.

This book will be given away for free to generate leads for a financial services firm. Needs to be very visual and eye-catching (colorful)

Target Market(s)

Millenials and young working adults

Font styles to use
Sans Serif

Requirements
Must have
• Some elements of debt converting into money. Maybe things like credit cards and cars and student loans going through something and coming out the other side as paper currency

Author names on front cover in a darker color bar at bottom of cover

Pictures of me and co-author with short bios on the back. Can be in a darker background than the front cover

Like a white or light colored background

Title and Author names on the spine
Should not have
• No busy graphics

```html
<!DOCTYPE html>
<html lang="en">
<head>
<meta charset="utf-8">
<title>Painting Storms over Harbors – Book Cover Wrap</title>
<link href="https://fonts.googleapis.com/css2?family=Anton&family=Open+Sans:wght@300;400&display=swap" rel="stylesheet">
<style>
  :root {
    --backdrop: #c4c4c4;
    --back-green: #c4e09a;
    --cover-white: #ffffff;
    --cover-shade: #e6e6e6;
    --ink: #0b0b0b;
    --accent-red: #e30613;
    --spine-white: #f7f7f7;
    --box-white: #ffffff;
    --art-blue: #8fb4dc;
    --art-navy: #1d2a44;
    --art-cream: #d9d6c3;
  }
  * { box-sizing: border-box; margin: 0; padding: 0; }
  html, body {
    width: 1200px; height: 800px; overflow: hidden;
    background: var(--backdrop);
  }
  .wrap {
    position: absolute; left: 212px; top: 130px;
    width: 776px; height: 540px;
    display: flex;
    box-shadow: 0 10px 30px rgba(0,0,0,.25);
  }

  /* Back cover */
  .back-cover {
    width: 360px; height: 100%;
    background: var(--back-green);
    padding: 30px 26px 24px 30px;
    position: relative;
    font-family: "Open Sans", sans-serif;
    color: var(--ink);
  }
  .back-title {
    font-family: "Anton", sans-serif;
    font-weight: 400;
    font-size: 21px; line-height: 1;
    letter-spacing: .2px;
    text-transform: uppercase;
    margin-bottom: 14px;
  }
  .accent { color: var(--accent-red); }
  .blurb {
    font-size: 8.4px; line-height: 1.32;
    margin-bottom: 16px;
  }
  .bio {
    display: flex; gap: 14px; align-items: center;
    margin-bottom: 18px;
  }
  .bio .blurb { margin-bottom: 0; flex: 1; }
  .author-photo {
    width: 58px; height: 58px; flex: none;
    background: var(--box-white);
  }
  .barcode-box {
    position: absolute; right: 26px; bottom: 26px;
    width: 120px; height: 70px;
    background: var(--box-white);
  }

  /* Spine */
  .spine {
    width: 46px; height: 100%;
    background: var(--spine-white);
    display: flex; flex-direction: column; align-items: center;
    justify-content: space-between;
    padding: 26px 0 30px;
    writing-mode: vertical-rl;
  }
  .spine-title {
    font-family: "Anton", sans-serif;
    font-size: 19px; letter-spacing: .3px;
    text-transform: uppercase; color: var(--ink);
  }
  .spine-author {
    font-family: "Open Sans", sans-serif; font-weight: 300;
    font-size: 13px; letter-spacing: 3px; color: var(--ink);
  }

  /* Front cover */
  .front-cover {
    width: 370px; height: 100%;
    background: radial-gradient(ellipse at 60% 40%, var(--cover-white) 40%, var(--cover-shade) 100%);
    position: relative;
    border-left: 1px solid #dcdcdc;
  }
  .front-title {
    position: absolute; left: 34px; top: 70px; width: 310px;
    font-family: "Anton", sans-serif; font-weight: 400;
    text-transform: uppercase; line-height: .92; color: var(--ink);
  }
  .front-title .line-1 { display: block; font-size: 52px; }
  .front-title .line-2 { display: block; font-size: 38px; padding-left: 58px; }
  .front-title .line-3 { display: block; font-size: 78px; color: var(--accent-red); letter-spacing: 1px; }
  .cover-art {
    position: absolute; left: 70px; top: 290px;
    width: 230px; height: 160px;
    border-radius: 6px;
    background: linear-gradient(135deg, var(--art-blue) 0%, var(--art-cream) 55%, var(--art-navy) 100%);
  }
  .front-author {
    position: absolute; left: 0; right: 0; bottom: 36px;
    text-align: center;
    font-family: "Open Sans", sans-serif; font-weight: 300;
    font-size: 21px; letter-spacing: 4px; color: var(--ink);
  }
</style>
</head>
<body>
  <main class="wrap">
    <section class="back-cover">
      <h2 class="back-title">Painting Storms over <span class="accent">Harbors</span></h2>
      <p class="blurb">Lorem ipsum dolor sit amet, consectetur adipiscing elit, sed do eiusmod tempor incididunt ut labore et dolore magna aliqua. Ut enim ad minim veniam, quis nostrud exercitation ullamco laboris nisi ut aliquip ex ea commodo consequat. Duis aute irure dolor in reprehenderit in voluptate velit esse cillum dolore eu fugiat nulla pariatur. Excepteur sint occaecat cupidatat non proident, sunt in culpa qui officia deserunt mollit anim id est laborum.</p>
      <p class="blurb">Lorem ipsum dolor sit amet, consectetur adipiscing elit, sed do eiusmod tempor incididunt ut labore et dolore magna aliqua. Ut enim ad minim veniam, quis nostrud exercitation ullamco laboris nisi ut aliquip ex ea commodo consequat. Duis aute irure dolor in reprehenderit in voluptate velit esse cillum dolore eu fugiat nulla pariatur. Excepteur sint occaecat cupidatat non proident, sunt in culpa qui officia deserunt mollit anim id est laborum.</p>
      <div class="bio">
        <div class="author-photo" aria-label="Author photo placeholder"></div>
        <p class="blurb">Lorem ipsum dolor sit amet, consectetur adipiscing elit, sed do eiusmod tempor incididunt ut labore et dolore magna aliqua. Ut enim ad minim veniam, quis nostrud exercitation ullamco laboris nisi ut aliquip ex ea commodo consequat. Duis aute irure dolor in reprehenderit in voluptate velit esse cillum dolore eu fugiat nulla pariatur. Excepteur sint occaecat cupidatat non proident, sunt in culpa qui officia deserunt mollit anim id est laborum.</p>
      </div>
      <div class="bio">
        <div class="author-photo" aria-label="Co-author photo placeholder"></div>
        <p class="blurb">Lorem ipsum dolor sit amet, consectetur adipiscing elit, sed do eiusmod tempor incididunt ut labore et dolore magna aliqua. Ut enim ad minim veniam, quis nostrud exercitation ullamco laboris nisi ut aliquip ex ea commodo consequat. Duis aute irure dolor in reprehenderit in voluptate velit esse cillum dolore eu fugiat nulla pariatur. Excepteur sint occaecat cupidatat non proident, sunt in culpa qui officia deserunt mollit anim id est laborum.</p>
      </div>
      <div class="barcode-box"></div>
    </section>

    <section class="spine">
      <span class="spine-title">Painting Storms over <span class="accent">Harbors</span></span>
      <span class="spine-author">AUTHOR NAME</span>
    </section>

    <section class="front-cover">
      <h1 class="front-title">
        <span class="line-1">Painting</span>
        <span class="line-2">Storms over</span>
        <span class="line-3">Harbors</span>
      </h1>
      <div class="cover-art" role="img" aria-label="Photo of a fanned stack of bank cards with crumpled paper banknotes on top"></div>
      <p class="front-author">AUTHOR NAME</p>
    </section>
  </main>
</body>
</html>
```